Business Card desgin, company called Stand Fast.

I am looking for the logo colors (3) to be used on the card in whatever design you think might work. the certifications are on the back (4) on the front will be my name, Dana Whitlock, owner/instructor, phone 208.555.0193, website www.sfx-drills.example, email dw@sfx-drills.example. im flexible on fonts.

Target Market(s)

firearms owners

Industry/Entity Type

firearms training

Contact Information for Business Card

certification icons on back

```html
<!DOCTYPE html>
<html lang="en">
<head>
<meta charset="utf-8">
<title>Stand Fast — Business Card</title>
<link rel="stylesheet" href="https://fonts.googleapis.com/css2?family=Quicksand:wght@400;500;700&family=Montserrat:wght@600;700&display=swap">
<style>
  :root {
    --navy: #0e2942;
    --red: #b91f2e;
    --white: #ffffff;
    --ground: #cccccc;
    --badge: #6f7c88;
  }
  * { box-sizing: border-box; margin: 0; padding: 0; }
  html, body { width: 1200px; height: 1112px; overflow: hidden; background: var(--ground); }
  .canvas { position: relative; width: 1200px; height: 1112px; }

  .card { position: absolute; width: 753px; height: 443px; background: var(--white); overflow: hidden; }
  .card--back { left: 75px; top: 75px; }
  .card--front { left: 372px; top: 593px; }

  /* back side */
  .back-panel { position: absolute; left: 0; top: 0; width: 376px; height: 443px; background: var(--navy); }
  .back-band { position: absolute; left: 0; top: 90px; width: 376px; height: 263px; background: var(--red); }
  .back-seal { position: absolute; left: 237px; top: 89px; width: 264px; height: 264px; border-radius: 50%; background: var(--red); }
  .back-seal__inner {
    position: absolute; left: 10px; top: 10px; width: 244px; height: 244px; border-radius: 50%;
    background: var(--navy); display: flex; flex-direction: column; align-items: center; justify-content: center;
  }
  .brand-name { font-family: "Montserrat", sans-serif; font-weight: 700; color: var(--red); font-size: 18px; letter-spacing: 0.02em; text-transform: uppercase; }
  .brand-mark { width: 92px; height: 92px; border-radius: 50%; border: 5px solid var(--white); margin: 16px 0 18px; }
  .brand-url { font-family: "Montserrat", sans-serif; font-weight: 700; color: var(--white); font-size: 7.5px; letter-spacing: 0.03em; text-transform: uppercase; }

  .cert-list { position: absolute; left: 676px; top: 40px; display: flex; flex-direction: column; gap: 38px; }
  .cert-badge { display: block; width: 60px; height: 62px; }

  /* front side */
  .front-panel { position: absolute; left: 379px; top: 0; width: 374px; height: 443px; background: var(--navy); }
  .front-stripe { position: absolute; left: 0; top: 386px; width: 753px; height: 12px; background: var(--red); }
  .person { position: absolute; left: 45px; top: 68px; font-family: "Quicksand", sans-serif; }
  .person__name { color: var(--navy); font-weight: 700; font-size: 31px; letter-spacing: 0.03em; line-height: 1.1; }
  .person__role { color: var(--red); font-weight: 500; font-size: 24px; line-height: 1.2; }

  .contact-list { position: absolute; left: 45px; top: 221px; list-style: none; font-family: "Quicksand", sans-serif; }
  .contact-item { display: flex; align-items: center; height: 39px; margin-bottom: 8px; color: var(--navy); font-size: 23px; font-weight: 500; }
  .contact-icon { width: 39px; height: 39px; border-radius: 50%; background: var(--red); display: flex; align-items: center; justify-content: center; margin-right: 10px; flex: none; }
  .contact-icon svg { width: 18px; height: 18px; }

  .front-brand { position: absolute; left: 379px; top: 0; width: 374px; height: 386px; display: flex; flex-direction: column; align-items: center; justify-content: center; gap: 14px; }
  .front-brand__mark { width: 118px; height: 118px; border-radius: 50%; border: 6px solid var(--white); }
  .front-brand__name { font-family: "Montserrat", sans-serif; font-weight: 700; font-size: 18px; color: var(--white); text-transform: uppercase; letter-spacing: 0.04em; }
</style>
</head>
<body>
<main class="canvas">

  <section class="card card--back" aria-label="Card back">
    <div class="back-panel"></div>
    <div class="back-band"></div>
    <div class="back-seal">
      <div class="back-seal__inner">
        <span class="brand-name">Stand Fast</span>
        <span class="brand-mark" aria-hidden="true"></span>
        <span class="brand-url">www.sfx-drills.example</span>
      </div>
    </div>
    <div class="cert-list">
      <svg class="cert-badge" viewBox="0 0 60 62" role="img" aria-label="Instructor certification badge"><path d="M12 2h36v40l-18 16-18-16z" fill="var(--navy)"/></svg>
      <svg class="cert-badge" viewBox="0 0 60 62" role="img" aria-label="Range safety officer certification badge"><path d="M4 4h52v34l-26 20-26-20z" fill="var(--badge)"/></svg>
      <svg class="cert-badge" viewBox="0 0 60 62" role="img" aria-label="Concealed carry instructor certification badge"><path d="M30 2l26 10v20c0 14-12 24-26 28C16 56 4 46 4 32V12z" fill="var(--red)"/></svg>
      <svg class="cert-badge" viewBox="0 0 60 62" role="img" aria-label="Tactical instructor certification badge"><path d="M30 2l27 10v20c0 14-12 24-27 28C15 56 3 46 3 32V12z" fill="#e8862a" stroke="var(--navy)" stroke-width="3"/></svg>
    </div>
  </section>

  <section class="card card--front" aria-label="Card front">
    <div class="front-panel"></div>
    <div class="front-brand">
      <span class="front-brand__mark" aria-hidden="true"></span>
      <span class="front-brand__name">Stand Fast</span>
    </div>
    <div class="front-stripe"></div>

    <div class="person">
      <h1 class="person__name">Dana Whitlock</h1>
      <p class="person__role">owner/instructor</p>
    </div>

    <ul class="contact-list">
      <li class="contact-item">
        <span class="contact-icon"><svg viewBox="0 0 24 24"><path d="M6.6 10.8a15 15 0 0 0 6.6 6.6l2.2-2.2c.3-.3.7-.4 1-.2 1.1.4 2.3.6 3.6.6.6 0 1 .4 1 1V20c0 .6-.4 1-1 1A17 17 0 0 1 3 4c0-.6.4-1 1-1h3.5c.6 0 1 .4 1 1 0 1.3.2 2.5.6 3.6.1.3 0 .7-.2 1z" fill="#fff"/></svg></span>
        208.555.0193
      </li>
      <li class="contact-item">
        <span class="contact-icon"><svg viewBox="0 0 24 24"><rect x="3" y="6" width="18" height="12" rx="1" fill="#fff"/><path d="M3.5 6.5l8.5 6.5 8.5-6.5" fill="none" stroke="var(--red)" stroke-width="1.6"/></svg></span>
        dw@sfx-drills.example
      </li>
      <li class="contact-item">
        <span class="contact-icon"><svg viewBox="0 0 24 24" fill="none" stroke="#fff" stroke-width="1.8"><circle cx="12" cy="12" r="8"/><path d="M4 12h16M12 4c3 3 3 13 0 16M12 4c-3 3-3 13 0 16"/></svg></span>
        www.sfx-drills.example
      </li>
    </ul>
  </section>

</main>
</body>
</html>
```